Brivet Networks, Inc. Website redesign

Revamp the website, it is old and outdated. www.brivetnetworksinc.com

Target Market(s)

Information Technology Consulting and Staffing

Coding

Coded - Design and coding required

Number of Pages Required

5+ page

Colors

Designer to choose colors to be used in the design.

Requirements
Must have
• Outlined text boxes just like from the Hollis.us site. A clean look

```html
<!DOCTYPE html>
<html lang="en">
<head>
<meta charset="utf-8">
<title>Brivet Networks, Inc.</title>
<link href="https://fonts.googleapis.com/css2?family=Rajdhani:wght@500;600;700&family=Josefin+Sans:wght@300;400;600&display=swap" rel="stylesheet">
<style>
:root{
  --red:#a3172d;
  --red-bright:#e3203f;
  --ink:#1d1f22;
  --text:#6c6f73;
  --soft:#f2f2f4;
  --footer:#1e2125;
  --footer-bar:#27292d;
  --footer-text:#b9bcc0;
  --social:#1f4f8e;
}
*{margin:0;padding:0;box-sizing:border-box}
html,body{width:1200px;height:3771px;overflow:hidden;background:#fff}
body{position:relative;font-family:"Josefin Sans",sans-serif;color:var(--text)}
.abs{position:absolute}
h2,.display{font-family:"Rajdhani",sans-serif;font-weight:700;color:var(--ink);letter-spacing:.5px}
.section-title{position:absolute;left:0;width:1200px;text-align:center;font-size:38px;line-height:1}
.btn{position:absolute;background:var(--red);color:#fff;font-family:"Rajdhani",sans-serif;font-weight:600;font-size:10px;letter-spacing:.5px;height:24px;line-height:25px;text-align:center;text-transform:uppercase}
.para{font-size:11.5px;line-height:21px;font-weight:300}

/* header */
.brand{left:94px;top:24px;display:flex;align-items:center;gap:10px}
.brand-mark{width:14px;height:14px;background:var(--red)}
.brand-name{font-family:"Rajdhani",sans-serif;font-weight:700;font-size:20px;color:var(--ink)}
.tagline{left:218px;top:32px;font-size:12px;font-variant:small-caps;color:#666;letter-spacing:.3px}
.topbar{right:94px;top:11px;font-size:10.5px;color:var(--ink);display:flex;gap:16px}
.topbar span b{color:var(--red);font-weight:400}
.nav{right:94px;top:53px;display:flex;gap:44px;font-family:"Rajdhani",sans-serif;font-weight:600;font-size:10px;color:#333}
.nav .active{color:var(--red)}

/* hero */
.hero{left:0;top:84px;width:1200px;height:516px}
.hero-text{left:732px;top:252px}
.hero-kicker{font-family:"Rajdhani",sans-serif;font-weight:600;font-size:27px;color:#fff;letter-spacing:.5px}
.hero-title{font-family:"Rajdhani",sans-serif;font-weight:700;font-size:70px;line-height:62px;color:var(--red-bright);letter-spacing:1px}
.hero-sub{font-family:"Rajdhani",sans-serif;font-weight:600;font-size:19px;color:#fff;letter-spacing:4.5px;margin-top:6px}

/* services */
.service{position:absolute;top:780px;width:230px;text-align:center}
.service svg{display:block;margin:0 auto}
.service h3{font-family:"Rajdhani",sans-serif;font-weight:600;font-size:16px;color:var(--ink);margin-top:14px}
.service p{font-size:10px;line-height:16.5px;font-weight:300;margin-top:12px;height:68px}
.service .btn{position:relative;display:inline-block;width:80px;margin-top:14px}

/* about */
.about-band{left:0;top:1124px;width:1200px;height:358px;background:var(--soft)}
.about-photo{left:0;top:1124px;width:575px;height:358px}
.eyebrow{font-family:"Rajdhani",sans-serif;font-weight:500;font-size:20px;color:#444;letter-spacing:.5px}
.big{font-family:"Rajdhani",sans-serif;font-weight:700;font-size:39px;color:var(--ink);line-height:1;letter-spacing:.5px}

/* leaders */
.leader-photo{left:553px;top:1640px;width:92px;height:133px;background:linear-gradient(160deg,#777,#ddd 60%,#999)}
.leader-name{left:0;top:1796px;width:1200px;text-align:center;font-size:14px;color:#333;letter-spacing:.3px}
.leader-name b{font-weight:600;color:var(--ink)}
.dots{left:589px;top:1948px;display:flex;gap:5px}
.dots i{width:4px;height:4px;border-radius:50%;background:#ccc}
.dots i:first-child{background:#333}

/* news */
.card{position:absolute;top:2686px;width:325px}
.card .thumb{width:325px;height:232px}
.card .date{font-size:10.5px;margin-top:18px;color:#888}
.card h4{font-family:"Josefin Sans",sans-serif;font-weight:400;font-size:17px;line-height:22px;color:var(--ink);margin-top:14px}
.card p{font-size:11.5px;line-height:20px;font-weight:300;margin-top:14px}
.card .btn{position:relative;display:inline-block;width:78px;margin-top:14px}

/* footer */
.footer{left:0;top:3223px;width:1200px;height:548px;background:var(--footer)}
.contact{position:absolute;top:3270px;width:240px;text-align:center;color:#fff;font-size:11px;line-height:15px}
.contact svg{display:block;margin:0 auto 14px}
.rule{left:94px;top:3350px;width:1012px;height:1px;background:#34373b}
.col{position:absolute;top:3386px;color:var(--footer-text);font-size:11px}
.col h5{font-family:"Rajdhani",sans-serif;font-weight:700;font-size:16px;color:#fff;letter-spacing:.5px;margin-bottom:14px}
.col li{list-style:none;line-height:27px}
.vline{position:absolute;top:3352px;width:1px;height:280px;background:#2e3135}
.field{position:absolute;left:926px;width:180px;height:30px;border:1px solid #3c3f44;font-size:8.5px;color:#888;padding:11px 10px 0}
.subscribe{left:926px;top:3521px;width:180px;height:30px;background:var(--red);color:#fff;font-family:"Rajdhani",sans-serif;font-weight:600;font-size:11px;text-align:center;line-height:31px;letter-spacing:.5px}
.social{left:94px;top:3634px;width:1012px;height:48px;display:flex;background:var(--footer-bar)}
.social div{flex:1;text-align:center;line-height:49px;color:#d6d8da;font-size:12.5px;letter-spacing:.3px}
.social .on{background:var(--social);color:#fff}
.social .on i{display:inline-block;width:14px;height:14px;border-radius:50%;background:#fff;vertical-align:-2px;margin-right:6px}
.copy{left:0;top:3716px;width:1200px;text-align:center;font-size:10px;color:#8b8e92}
.copy b{color:#fff;font-weight:600}
</style>
</head>
<body>

<!-- header -->
<div class="abs brand"><span class="brand-name">BRIVET</span><span class="brand-mark"></span></div>
<div class="abs tagline">Mission Integrity Results</div>
<div class="abs topbar"><span><b>☎ Call Us:</b> 301-555-0142</span><span><b>✉ Mail Us:</b> info@brivetnetworksinc.com</span></div>
<nav class="abs nav"><span class="active">HOME</span><span>ABOUT US</span><span>SERVICES</span><span>STRATEGY</span><span>IT NEWS</span><span>CONTACT US</span></nav>

<!-- hero -->
<svg class="abs hero" viewBox="0 0 1200 516" role="img" aria-label="Close-up photo of network cables plugged into a switch panel">
  <defs>
    <linearGradient id="heroFill" x1="0" y1="0" x2="1" y2="1">
      <stop offset="0" stop-color="#3a4150"/>
      <stop offset=".45" stop-color="#6f7785"/>
      <stop offset="1" stop-color="#1c2029"/>
    </linearGradient>
  </defs>
  <path d="M140 0H1200V516H0V260C10 130 60 40 140 0Z" fill="url(#heroFill)"/>
</svg>
<div class="abs hero-text">
  <div class="hero-kicker">BRINGING THOUGHT</div>
  <div class="hero-title">LEADERSHIP</div>
  <div class="hero-sub">&amp; QUALITY TO EVERY PROJECT</div>
</div>

<!-- services -->
<h2 class="section-title" style="top:698px">OUR SERVICES</h2>

<div class="service" style="left:106px">
  <svg width="80" height="92" viewBox="0 0 80 92"><rect x="22" y="12" width="26" height="34" fill="none" stroke="#222" stroke-width="2"/><path d="M48 18a14 14 0 0 1 0 24" fill="none" stroke="#222" stroke-width="2"/><rect x="30" y="36" width="10" height="10" fill="none" stroke="#e0a400" stroke-width="2"/><path d="M10 62l30 16 30-16" fill="none" stroke="var(--red)" stroke-width="6"/></svg>
  <h3>Hardware / Software Sales</h3>
  <p>We have access to multiple distributor partners throughout North America, as well as Elite Partner Status with many of the industry's marquee manufacturers...</p>
  <span class="btn">Read More</span>
</div>
<div class="service" style="left:358px">
  <svg width="80" height="92" viewBox="0 0 80 92"><circle cx="36" cy="24" r="9" fill="#222"/><path d="M20 56c0-14 8-20 16-20s16 6 16 20z" fill="#222"/><circle cx="54" cy="14" r="9" fill="#e0a400"/><path d="M10 62l30 16 30-16" fill="none" stroke="var(--red)" stroke-width="6"/></svg>
  <h3>Professional Services</h3>
  <p>Our team provides experienced leadership and guidance, utilizing the industry standard methodologies. We help you maintain a comprehensive view of strategy...</p>
  <span class="btn">Read More</span>
</div>
<div class="service" style="left:612px">
  <svg width="80" height="92" viewBox="0 0 80 92"><circle cx="34" cy="28" r="14" fill="none" stroke="#222" stroke-width="2"/><circle cx="48" cy="22" r="9" fill="none" stroke="#e0a400" stroke-width="3"/><path d="M28 44h12v8H28z" fill="#222"/><path d="M10 62l30 16 30-16" fill="none" stroke="var(--red)" stroke-width="6"/></svg>
  <h3>Technology Assessment</h3>
  <p>Experience has shown companies that perform objective, third-party technology assessments have proven to be instrumental in identifying weaknesses...</p>
  <span class="btn">Read More</span>
</div>
<div class="service" style="left:865px">
  <svg width="80" height="92" viewBox="0 0 80 92"><rect x="28" y="16" width="24" height="24" fill="none" stroke="#222" stroke-width="2"/><circle cx="40" cy="28" r="6" fill="#e0a400"/><path d="M28 22H16M28 34H16M52 22h12M52 34h12M34 16V6M46 16V6M34 40v8M46 40v8" stroke="#222" stroke-width="2"/><path d="M10 62l30 16 30-16" fill="none" stroke="var(--red)" stroke-width="6"/></svg>
  <h3>Technology Consulting</h3>
  <p>Implementing quality solutions is more than applying technology to problems. You need experts with deep technical knowledge and broad industry experience...</p>
  <span class="btn">Read More</span>
</div>

<!-- about -->
<div class="abs about-band"></div>
<svg class="abs about-photo" viewBox="0 0 575 358" role="img" aria-label="Photo of an engineer using a tablet beside a server rack">
  <defs><linearGradient id="aboutFill" x1="0" y1="0" x2="1" y2="0"><stop offset="0" stop-color="#1c3a63"/><stop offset=".6" stop-color="#4a6a8e"/><stop offset="1" stop-color="#a9b3bd"/></linearGradient></defs>
  <polygon points="0,0 575,0 575,358 0,358" fill="url(#aboutFill)"/>
  <polygon points="465,0 575,110 575,358 530,358 530,120 420,0" fill="var(--red)"/>
</svg>
<div class="abs" style="left:629px;top:1158px">
  <div class="eyebrow">ABOUT OUR</div>
  <div class="big" style="margin-top:8px">BRIVET NETWORKS</div>
  <p class="para" style="width:480px;margin-top:18px">Brivet Networks, Inc. is an 8(a) innovative and rapidly growing full-service IT consulting firm. We provide our clients with cutting-edge technologies and the know-how to apply them to their individual business models.</p>
  <p class="para" style="width:480px;margin-top:10px">For over 20 + years, we have been providing reliable IT solutions to businesses in the Washington, DC Metro area and beyond. Our comprehensive services provide clients with unique technology solutions that are customized to meet the specific demands of their business.</p>
</div>
<span class="btn" style="left:629px;top:1421px;width:78px">Read More</span>

<!-- leaders -->
<h2 class="section-title" style="top:1581px">OUR LEADERS</h2>
<div class="abs leader-photo" role="img" aria-label="Portrait photo of the co-founder"></div>
<div class="abs leader-name"><b>ROHAN KESARI</b> – CO-FOUNDER</div>
<p class="abs para" style="left:195px;top:1824px;width:810px;text-align:center">Rohan has played a leading role in the global information technology industry for more than 20 years, managing divisions and business the United States. Since founding Brivet Networks, Inc. (BNI) in 2008, he has been instrumental in formulating the company's strategy and building and managing the organization's core competencies.</p>
<span class="btn" style="left:561px;top:1903px;width:78px">Read More</span>
<div class="abs dots"><i></i><i></i><i></i></div>

<!-- strategy -->
<svg class="abs" style="left:0;top:1985px" width="1200" height="600" viewBox="0 0 1200 600">
  <defs><linearGradient id="stratFill" x1="0" y1="0" x2="1" y2="0"><stop offset="0" stop-color="#d8e2ee"/><stop offset=".5" stop-color="#4f6f96"/><stop offset="1" stop-color="#1b2b45"/></linearGradient></defs>
  <polygon points="0,10 600,95 1200,10 1200,580 600,510 0,600" fill="#f3f4f8"/>
  <polygon points="0,0 600,95 0,22" fill="var(--red)"/>
  <polygon points="1200,0 1200,22 600,95" fill="var(--red)"/>
  <polygon points="0,575 600,505 0,600" fill="#e2e3e7"/>
  <polygon points="1200,565 1200,590 600,505" fill="#e2e3e7"/>
  <polygon points="600,95 1200,20 1200,565 600,505" fill="url(#stratFill)" role="img" aria-label="Photo of a technician with a laptop in a data centre aisle"/>
</svg>
<div class="abs" style="left:95px;top:2106px">
  <div class="eyebrow">OUR STRATEGY</div>
  <div class="big" style="margin-top:8px">YOUR PATH TO SUCCESS</div>
  <p class="para" style="width:450px;margin-top:18px">Civilian and Federal agencies are facing increased demands driven by the changing economic environment and shifts in the way products and services are sold and delivered. These factors have created an imperative to leverage new and innovative technology solution architectures like cloud computing to help reduce cost and deliver profit-driving IT capabilities faster than ever before. Savvy businesses understand that technology investments cannot be made solely to enable internal and external operations; technology is now, more than ever, a critical component to retaining and winning customers as well as staying ahead of the competition.</p>
</div>
<span class="btn" style="left:95px;top:2403px;width:80px">Read More</span>

<!-- news -->
<h2 class="section-title" style="top:2618px">LATEST IT NEWS</h2>
<div class="card" style="left:94px">
  <div class="thumb" role="img" aria-label="Photo of a hand holding a phone beside a router and laptop" style="background:linear-gradient(135deg,#e9e6e2,#9a9694)"></div>
  <div class="date">17TH AUGUST, 2019</div>
  <h4>There are many variations of passages of Lorem Ipsum</h4>
  <p>If you use this site regularly and would like to help keep the site on the Internet, please consider donating a small sum...</p>
  <span class="btn">Read More</span>
</div>
<div class="card" style="left:438px">
  <div class="thumb" role="img" aria-label="Photo of a network cable being plugged into a laptop" style="background:linear-gradient(135deg,#f1f1f1,#c8c8cc 60%,#8f8a88)"></div>
  <div class="date">17TH AUGUST, 2019</div>
  <h4>There are many variations of passages of Lorem Ipsum</h4>
  <p>If you use this site regularly and would like to help keep the site on the Internet, please consider donating a small sum...</p>
  <span class="btn">Read More</span>
</div>
<div class="card" style="left:781px">
  <div class="thumb" role="img" aria-label="Photo of a businessman with a tablet in a server room" style="background:linear-gradient(135deg,#2b3d5c,#7d8ea6 55%,#c9cdd4)"></div>
  <div class="date">17TH AUGUST, 2019</div>
  <h4>There are many variations of passages of Lorem Ipsum</h4>
  <p>If you use this site regularly and would like to help keep the site on the Internet, please consider donating a small sum...</p>
  <span class="btn">Read More</span>
</div>

<!-- footer -->
<div class="abs footer"></div>
<div class="contact" style="left:101px">
  <svg width="18" height="24" viewBox="0 0 18 24"><path d="M9 0a9 9 0 0 1 9 9c0 7-9 15-9 15S0 16 0 9a9 9 0 0 1 9-9z" fill="#fff"/><circle cx="9" cy="9" r="3.5" fill="var(--footer)"/></svg>
  2480 Larkstone Dr Ashgrove,<br>MD 20900
</div>
<div class="contact" style="left:355px">
  <svg width="22" height="24" viewBox="0 0 22 24"><path d="M5 1l4 5-3 3c2 4 4 6 8 8l3-3 5 4-3 5C10 22 0 12 1 4z" fill="#fff"/></svg>
  301-555-0142
</div>
<div class="contact" style="left:608px">
  <svg width="30" height="22" viewBox="0 0 30 22"><rect x="1" y="1" width="28" height="20" fill="none" stroke="#fff" stroke-width="2"/><path d="M1 1l14 11L29 1" fill="none" stroke="#fff" stroke-width="2"/></svg>
  info@brivetnetworks.com
</div>
<div class="contact" style="left:861px">
  <svg width="28" height="24" viewBox="0 0 28 24"><ellipse cx="12" cy="10" rx="10" ry="7" fill="none" stroke="var(--red-bright)" stroke-width="2"/><path d="M6 16l-3 5 7-3" fill="none" stroke="var(--red-bright)" stroke-width="2"/><path d="M22 8c4 1 5 4 4 7l1 4-4-2" fill="none" stroke="var(--red-bright)" stroke-width="2"/></svg>
  Live Chat
</div>
<div class="abs rule"></div>
<div class="vline" style="left:348px"></div>
<div class="vline" style="left:603px"></div>
<div class="vline" style="left:857px"></div>
<div class="col" style="left:95px"><h5>QUICK LINKS</h5><ul><li>Home</li><li>About us</li><li>Services</li><li>Strategy</li><li>IT News</li><li>Contact us</li></ul></div>
<div class="col" style="left:384px;top:3386px"><h5>SERVICES</h5><ul><li>Hardware / Software Sales</li><li>Professional Services</li><li>Technology Assessment</li><li>Technology Consulting</li></ul></div>
<div class="col" style="left:689px"><h5>IT STRATEGY</h5><ul><li>Assess</li><li>Recommend</li><li>Implement</li><li>Monitor</li><li>Manage</li></ul></div>
<div class="col" style="left:926px"><h5>NEWSLETTER</h5></div>
<div class="field" style="top:3450px">Enter Name:</div>
<div class="field" style="top:3486px">Enter Email:</div>
<div class="abs subscribe">SUBSCRIBE</div>
<div class="abs social"><div class="on"><i></i>CIRCLEBOOK</div><div>CHIRPER</div><div>BLOG</div><div>WORKFOLIO</div></div>
<div class="abs copy">COPYRIGHT © 2019 <b>BRIVET NETWORKS</b>. ALL RIGHTS RESERVED.</div>

</body>
</html>
```